Web page Skin for music publishing company

We need a logo and a web page skin for a music publishing company. "Rusty Canvas" is it's name. The company showcases writers of country music in Nashville.

With the name Rusty Canvas we would like to keep the denim look somehow.

Logo should clearly explain the company and reflect the business.

Page should have basic elements - About Us, Our Music, Who We Are, Contact Us, etc.

Maybe use buttons or tags for navigation elements?

Project requires a logo and a website.

This is denim: https://www.searchvolt.example/url?sa=i&rct=j&q=&esrc=s&source=images&cd=&cad=rja&uact=8&docid=72k9pTqarsWvXe&tbnid=KQT4HmWzaP28TR:&ved=0CAUQkTx&url=http%3A%2F%2Ffabricseekers.example%2F2013%2F05%2Fguide-how-to-date-old-work-trousers%2F&ei=ZZ48K2DkMPuv7BQr2HToWq&bvm=bv.41288176,d.qRt&psig=BXRmPLFHU-dMnw3Vq7SKfh8TgaYBZ2oWc&ust=1400336000039471

We would like to see more "old", and less new denim.

http://www.theagedclosethall.example/blog/wp-content/uploads/2011/02/IMG_0473_low_res.jpg

http://static8.pixelvaultstock.example/2759183/416/i/950/pixelvaultstock_6172409-Jeans-texture.jpg

http://img.bidmarrow.example/imgdata/4/2/7/8/3/9/1/webimg/914
382915_tp.jpghttp://www.stylequilt.example/cgi/img-thing?.out=jpg&size=l&tid=205917463

musicians, record companies, fans

Publishing Company

• Rusty Canvas look / background
Clear navigation

```html
<!DOCTYPE html>
<html lang="en">
<head>
<meta charset="utf-8">
<title>Rusty Canvas — Music Publishing</title>
<link rel="stylesheet" href="https://fonts.googleapis.com/css2?family=Bebas+Neue&display=swap">
<style>
  :root {
    --orange: #ff7200;
    --teal: #0f7276;
    --purple: #a015c0;
    --green: #1a9a12;
    --red: #b5121b;
    --wall-light: #9a9a9a;
    --wall-dark: #6e6e6e;
    --ink: #000;
    --panel: #5f5e60;
    --panel-top: #727173;
    --body-text: #a8a8a8;
    --rule: #2a2a2a;
    --white: #fff;
    --copy: #444;
    --social: #2b2b2b;
  }
  * { margin: 0; padding: 0; box-sizing: border-box; }
  html, body { width: 1200px; height: 1178px; overflow: hidden; }
  body {
    position: relative;
    font-family: Arial, Helvetica, sans-serif;
    background:
      linear-gradient(to bottom, var(--wall-light) 0, #8c8c8c 420px, var(--wall-dark) 640px, #2e2e2e 740px, var(--ink) 785px, var(--ink) 100%);
  }
  .display { font-family: "Bebas Neue", Impact, sans-serif; font-weight: 400; }

  .brand {
    position: absolute; left: 148px; top: 28px;
    display: flex; align-items: center; gap: 18px;
  }
  .brand-dot { width: 84px; height: 84px; border-radius: 50%; background: var(--orange); }
  .brand-name { font-size: 82px; line-height: 1; color: var(--orange); letter-spacing: 1px; }

  .main-nav { position: absolute; top: 131px; left: 0; }
  .main-nav a {
    position: absolute; top: 0; width: 142px; height: 47px;
    display: flex; align-items: center; justify-content: center;
    color: var(--white); text-decoration: none; font-size: 27px; padding-top: 3px;
    text-shadow: 1px 2px 2px rgba(0,0,0,.55);
  }
  .nav-home { left: 120px; background: var(--orange); }
  .nav-about { left: 282px; background: var(--teal); }
  .nav-music { left: 441px; background: var(--purple); }
  .nav-who { left: 601px; background: var(--green); }
  .nav-contact { left: 761px; background: var(--red); }

  .hero {
    position: absolute; left: 120px; top: 204px; width: 960px; height: 468px;
    border: 3px solid var(--orange);
    background: radial-gradient(ellipse at 55% 55%, #3a2a20 0, #1c1a19 45%, #0c0c0c 100%);
  }
  .hero-arrow { position: absolute; top: 198px; }
  .hero-arrow.prev { left: 18px; }
  .hero-arrow.next { right: 18px; }

  .content {
    position: absolute; left: 121px; top: 684px; width: 958px; height: 412px;
    background: linear-gradient(to bottom, var(--panel-top) 0, var(--panel) 90px);
  }
  .section-title { font-size: 35px; line-height: 1; color: var(--white); }
  .section-title span { color: var(--orange); }
  .welcome { position: absolute; left: 22px; top: 28px; width: 580px; }
  .welcome p { margin-top: 10px; font-size: 14px; line-height: 24px; color: var(--body-text); }
  .read-more { display: inline-block; margin-top: 6px; margin-left: 1px; font-size: 14px; color: var(--orange); text-decoration: none; }
  .divider { position: absolute; left: 636px; top: 28px; width: 1px; height: 360px; background: var(--rule); }

  .news { position: absolute; left: 683px; top: 28px; width: 260px; }
  .news-item { position: absolute; left: 0; width: 260px; }
  .news-thumb { position: absolute; left: 2px; top: 17px; width: 58px; height: 56px; background: linear-gradient(135deg, #1a1a1a, #5a4a3c 60%, #222); }
  .news-body { position: absolute; left: 78px; top: 12px; width: 185px; }
  .news-body h3 { font-size: 14px; font-weight: 400; color: var(--white); line-height: 18px; }
  .news-body p { font-size: 14px; line-height: 24px; color: var(--body-text); margin-top: 2px; }
  .news-body a { font-size: 14px; line-height: 22px; color: var(--orange); text-decoration: none; }
  .news-rule { position: absolute; left: 7px; width: 251px; height: 1px; background: var(--rule); }

  .footer-nav { position: absolute; left: 122px; top: 1118px; display: flex; gap: 12px; }
  .footer-nav a { font-size: 14px; color: var(--orange); text-decoration: none; }
  .copyright { position: absolute; left: 121px; top: 1145px; font-size: 14px; color: var(--copy); }
  .social { position: absolute; left: 906px; top: 1117px; display: flex; gap: 9px; }
  .social span { width: 34px; height: 34px; border-radius: 50%; background: var(--social); }
</style>
</head>
<body>
  <header class="brand">
    <span class="brand-dot"></span>
    <span class="brand-name display">Rusty Canvas</span>
  </header>

  <nav class="main-nav display">
    <a class="nav-home" href="#">Home</a>
    <a class="nav-about" href="#">About Us</a>
    <a class="nav-music" href="#">Our Music</a>
    <a class="nav-who" href="#">Who We Are</a>
    <a class="nav-contact" href="#">Contact</a>
  </nav>

  <section class="hero" role="img" aria-label="Slide photo: musician in a black hat and shirt playing a sunburst electric guitar on a dark backdrop">
    <svg class="hero-arrow prev" width="30" height="52" viewBox="0 0 30 52"><polyline points="26,2 4,26 26,50" fill="none" stroke="#555" stroke-width="5"/></svg>
    <svg class="hero-arrow next" width="30" height="52" viewBox="0 0 30 52"><polyline points="4,2 26,26 4,50" fill="none" stroke="#555" stroke-width="5"/></svg>
  </section>

  <main class="content">
    <article class="welcome">
      <h2 class="section-title display">Welcome to <span>our site!</span></h2>
      <p>Lorem ipsum dolor sit amet, conc tetur adipi scing. Praesent vestibuum molstie lacuiirhs. Aenean non ummy dreriauris. Phaselllus. porta. Fusce suscipit variusium sociis totdna tibus et magis dis parturient montes, nas.Lorem ipsum dolor sit amet, conc tetur adipi scing. Prae­sent vestibuum molstie lacuiirhs. Aenean non ummy dreriauris. Phaselllus. porta. Fusce suscipit variusium sociis totdna tibus et magis dis parturient montes, nas.Lorem ipsum dolor sit amet, conc tetur adipi scing. Praesent vestibuum molstie lacuiirhs. Aenean non ummy dreriauris. Phaselllus. porta. Fusce suscipit variusium sociis totdna tibus et magis dis parturi-</p>
      <a class="read-more" href="#">read more...</a>
    </article>

    <div class="divider"></div>

    <aside class="news">
      <h2 class="section-title display">Latest <span>news</span></h2>
      <div class="news-item" style="top:28px">
        <div class="news-thumb" role="img" aria-label="Thumbnail of a guitarist"></div>
        <div class="news-body"><h3>LOREM IPSUM DOLOR SIT</h3><p>Lorem ipsum dolor sit amet, conc tetur adipi</p><a href="#">more info</a></div>
      </div>
      <div class="news-rule" style="top:139px"></div>
      <div class="news-item" style="top:139px">
        <div class="news-thumb" role="img" aria-label="Thumbnail of a guitarist"></div>
        <div class="news-body"><h3>LOREM IPSUM DOLOR SIT</h3><p>Lorem ipsum dolor sit amet, conc tetur adipi</p><a href="#">more info</a></div>
      </div>
      <div class="news-rule" style="top:252px"></div>
      <div class="news-item" style="top:252px">
        <div class="news-thumb" role="img" aria-label="Thumbnail of a guitarist"></div>
        <div class="news-body"><h3>LOREM IPSUM DOLOR SIT</h3><p>Lorem ipsum dolor sit amet, conc tetur adipi</p><a href="#">more info</a></div>
      </div>
    </aside>
  </main>

  <footer>
    <nav class="footer-nav">
      <a href="#">HOME</a><a href="#">ABOUT US</a><a href="#">OUR MUSIC</a><a href="#">WHO WE ARE</a><a href="#">CONTACT</a>
    </nav>
    <p class="copyright">© 2014 rustycanvas .&nbsp; All Rights Reserved</p>
    <div class="social" aria-label="Social links"><span></span><span></span><span></span><span></span></div>
  </footer>
</body>
</html>
```